Harbor Lights (title of music CD cover)

Create a CD jacket (front and back). Front artwork will be used on CD itself.The CD is an EP (6 songs). They are all love songs (Ballads). Violin, cello, piano, percussion, acoustic guitar, that sort of sound. I am looking for a sophisticated look to the CD. The title is Harbor Lights and the subtitle is The Song of Two. The picture is of me; Lia Brandt. I want this CD jacket to exude class. I have uploaded an example of what i think i want. Obviously rough on my part.

Besides the attached picture of me, I am looking for: my name, name of Cd (Harbor Lights) and subtitle (The Song of Two)
on front of CD

Back:
1. Every Star Grew Quiet (Lia Brandt) 3:26
2. Like Fresh Rain (Lia Brandt) 3:20
3. Once Again Near (Lia Brandt) 4:00
4. The Evening (Lia Brandt) 3:53
5. Here & Always (Lia Brandt) 3:27
6. Harbor Lights (Lia Brandt / Dean Morrow) 4:28
Producer: Dean Morrow
© 2017 Blue Meadow Ventures, LLC

I have some more to go on back: barcode, publishing, additional credits
Updates

Target Market(s)

Adults 25-55

Industry/Entity Type

Music Download

Colors

Designer to choose colors to be used in the design.

Requirements
Must have
• Pic of me on front with title, subtitle and my name

```html
<!DOCTYPE html>
<html lang="en">
<head>
<meta charset="utf-8">
<title>Harbor Lights – The Song of Two – CD Jacket</title>
<link rel="stylesheet" href="https://fonts.googleapis.com/css2?family=Great+Vibes&family=Cinzel:wght@400&family=Open+Sans:ital@1&display=swap">
<style>
  :root {
    --backdrop: #e0c9b1;
    --label: #4a3a33;
    --sleeve: #0b0706;
    --gold: #d4a86e;
    --gold-soft: #c99d66;
    --ivory: #f3ece2;
    --track: #e8dfd3;
  }
  * { margin: 0; padding: 0; box-sizing: border-box; }
  html, body { width: 1200px; height: 848px; overflow: hidden; background: var(--backdrop); }
  .presentation { position: relative; width: 1200px; height: 848px; background: var(--backdrop); }

  .panel-label {
    position: absolute; top: 138px; width: 200px; margin-left: -100px;
    text-align: center; font: italic 400 32px "Open Sans", sans-serif; color: var(--label);
  }
  .panel-label--back { left: 370px; }
  .panel-label--front { left: 829px; }

  .sleeve {
    position: absolute; top: 222px; width: 404px; height: 404px;
    background: var(--sleeve); overflow: hidden;
  }
  .sleeve--back { left: 168px; }
  .sleeve--front { left: 628px; }

  /* back cover */
  .mic-photo {
    position: absolute; left: 26px; top: 110px; width: 214px; height: 270px;
    background: radial-gradient(ellipse at 40% 25%, #5a4530 0%, #2c2117 30%, #140e0a 60%, rgba(11,7,6,0) 80%);
  }
  .back-title {
    position: absolute; left: 44px; top: 14px; white-space: nowrap;
    color: var(--gold);
  }
  .back-title .script { font: 400 28px "Great Vibes", cursive; }
  .back-title .dash { font: 400 18px "Cinzel", serif; margin: 0 3px; }
  .back-title .subtitle { font: 400 21px "Cinzel", serif; }

  .tracklist { list-style: none; position: absolute; left: 0; top: 0; }
  .track {
    position: absolute; white-space: nowrap;
    font: 400 12.5px "Cinzel", serif; color: var(--track); letter-spacing: 0.02em;
  }
  .credits {
    position: absolute; left: 24px; top: 352px;
    font: 400 12.5px/19px "Cinzel", serif; color: var(--gold-soft);
  }

  /* front cover */
  .portrait-photo {
    position: absolute; inset: 0;
    background:
      radial-gradient(ellipse 55% 60% at 30% 40%, #8a6a48 0%, #4e3a27 35%, #1e1610 65%, rgba(11,7,6,0) 85%),
      linear-gradient(90deg, #1a120c 0%, #0b0706 70%);
  }
  .front-title {
    position: absolute; left: 168px; top: 40px; width: 230px;
    font: 400 66px/80px "Great Vibes", cursive; color: var(--ivory);
  }
  .front-title .line-two { display: block; padding-left: 22px; }
  .front-subtitle {
    position: absolute; left: 190px; top: 226px; width: 210px; text-align: center;
    font: 400 16px "Cinzel", serif; color: var(--gold);
  }
  .artist-name {
    position: absolute; left: 0; top: 344px; width: 404px; text-align: center;
    font: 400 28px "Cinzel", serif; color: var(--gold); letter-spacing: 0.42em;
    padding-left: 0.42em;
  }
</style>
</head>
<body>
<main class="presentation">
  <p class="panel-label panel-label--back">back</p>
  <p class="panel-label panel-label--front">front</p>

  <section class="sleeve sleeve--back" aria-label="Back cover">
    <div class="mic-photo" role="img" aria-label="Photograph of a vintage studio microphone in warm sepia tones"></div>
    <h2 class="back-title"><span class="script">Harbor Lights</span><span class="dash">-</span><span class="subtitle">The Song of Two</span></h2>
    <ol class="tracklist">
      <li class="track" style="left:46px;top:76px">1. Every Star Grew Quiet (Lia Brandt) 3:26</li>
      <li class="track" style="left:91px;top:98px">2. Like Fresh Rain (Lia Brandt) 3:20</li>
      <li class="track" style="left:115px;top:120px">3. Once Again Near (Lia Brandt) 4:00</li>
      <li class="track" style="left:137px;top:143px">4. The Evening (Lia Brandt) 3:53</li>
      <li class="track" style="left:149px;top:165px">5. Here &amp; Always (Lia Brandt) 3:27</li>
      <li class="track" style="left:166px;top:186px">6. Harbor Lights</li>
      <li class="track" style="left:170px;top:209px">(Lia Brandt / Dean Morrow) 4:28</li>
    </ol>
    <p class="credits">Producer: Dean Morrow<br>© 2017 Blue Meadow Ventures, LLC</p>
  </section>

  <section class="sleeve sleeve--front" aria-label="Front cover">
    <div class="portrait-photo" role="img" aria-label="Sepia portrait photograph of the artist"></div>
    <h1 class="front-title">Harbor <span class="line-two">Lights</span></h1>
    <p class="front-subtitle">The Song of Two</p>
    <p class="artist-name">LIA BRANDT</p>
  </section>
</main>
</body>
</html>
```